Toward Bright Morrow (TWBM) Business Card - company with a mission

Note* The file attached... orange with "Toward Bright MORROW" (in CAPS) is our logo. I am also open to having the text "toward bright morrow" OUTSIDE the orange round logo for business card (so yes, you may take the text out).

The info: (the following info are separate. So either you can use Martin or Helena for now, but that will be 2 separate cards, not together in one card. Thanks!!

Martin K Pardo
202.555.0183
martin@towardbrightmorrow.example
Managing Partner

Helena R Voss
202.555.0147
helena@towardbrightmorrow.example
Managing Partner

Our website: www.towardbrightmorrow.example

TWBM LLC stands for Toward Bright Morrow (non profit arm is called dawn lift foundation)—our business is based out of New York City and has a non-profit arm where for every bar of soap you purchase, we donate a bar (don’t want any designs that limits us to only soap). Currently working with South Africa. We want the focus to be organic/natural soap with a mission.

Looking for a clean, fresh design.

Industry/Entity Type

Non-Profit

Requirements
Must have
• Clean, fresh, refreshing. Design should not be too busy.

```html
<!DOCTYPE html>
<html lang="en">
<head>
<meta charset="utf-8">
<title>TWBM Business Card Options</title>
<link href="https://fonts.googleapis.com/css2?family=Jost:wght@300;400;500&display=swap" rel="stylesheet">
<style>
  :root {
    --teal: #93d6d0;
    --orange: #f5ac69;
    --white: #ffffff;
    --frame: #cdeeea;
  }
  * { box-sizing: border-box; margin: 0; padding: 0; }
  html, body { width: 1140px; height: 1200px; overflow: hidden; background: var(--white); }
  body { position: relative; font-family: "Jost", "Futura", sans-serif; color: var(--teal); }

  .column-label, .row-label { position: absolute; font-size: 17px; font-weight: 400; color: var(--teal); }
  .column-label { top: 80px; }
  .row-label { left: 182px; }

  .card {
    position: absolute; width: 320px; height: 194px;
    border: 1px solid var(--frame); background: var(--white); overflow: hidden;
  }
  .card--teal { background: var(--teal); border-color: var(--teal); }
  .col-a { left: 251px; }
  .col-b { left: 593px; }

  .brand-disc {
    position: absolute; left: 97px; width: 126px; height: 126px; border-radius: 50%;
    background: var(--orange); color: var(--white);
    display: flex; flex-direction: column; align-items: center; justify-content: center;
  }
  .brand-name { font-size: 40px; font-weight: 500; letter-spacing: 1px; line-height: 1; }
  .brand-tag { font-size: 10px; font-weight: 400; margin-top: 6px; }

  .card-url { position: absolute; left: 0; right: 0; text-align: center; font-size: 17px; }
  .card-tagline { position: absolute; left: 0; right: 0; text-align: center; font-size: 19px; font-weight: 500; }
  .card-tagline--spaced { font-size: 13px; letter-spacing: 4px; font-weight: 400; }

  .contact { position: absolute; right: 30px; text-align: right; font-weight: 300; font-size: 15px; line-height: 20px; }
  .contact .person { font-size: 18px; font-weight: 400; line-height: 22px; text-transform: uppercase; }
  .contact .site { font-size: 17px; font-weight: 400; }
  .card--teal .contact { color: var(--white); }

  .bubble-art {
    position: absolute; left: 0; bottom: 0; width: 132px; height: 70px;
    background: linear-gradient(90deg, rgba(255,255,255,0.55), rgba(255,255,255,0.15));
    border-top-right-radius: 60px;
  }
  .ribbon-art {
    position: absolute; left: 0; bottom: 0; width: 320px; height: 92px;
    background: linear-gradient(90deg, var(--orange), rgba(245,172,105,0.35));
    clip-path: polygon(0 0, 34% 0, 34% 62%, 100% 58%, 100% 70%, 34% 78%, 26% 100%, 0 100%);
  }
</style>
</head>
<body>
  <span class="column-label" style="left:443px;">A</span>
  <span class="column-label" style="left:695px;">B</span>

  <span class="row-label" style="top:252px;">1</span>
  <span class="row-label" style="top:477px;">2</span>
  <span class="row-label" style="top:730px;">3</span>
  <span class="row-label" style="top:994px;">4</span>

  <!-- Option 1 -->
  <section class="card col-a" style="top:162px;">
    <div class="brand-disc" style="top:19px;">
      <span class="brand-name">twbm</span>
      <span class="brand-tag">toward bright morrow</span>
    </div>
    <p class="card-url" style="top:152px;">www.twbm.example</p>
  </section>
  <section class="card card--teal col-b" style="top:162px;">
    <div class="contact" style="top:25px;">
      <p class="person">Martin K Pardo</p>
      <p>Managing Partner</p>
      <p>contact # 202-555-0147</p>
      <p>martin@twbm.example</p>
    </div>
    <div class="bubble-art" role="img" aria-label="Decorative outlined bubble circles in the lower left corner"></div>
  </section>

  <!-- Option 2 -->
  <section class="card col-a" style="top:395px;">
    <div class="brand-disc" style="top:17px;">
      <span class="brand-name">twbm</span>
    </div>
    <p class="card-tagline" style="top:150px;">toward bright morrow</p>
  </section>
  <section class="card col-b" style="top:395px;">
    <div class="contact" style="top:38px;">
      <p class="person">Martin K Pardo</p>
      <p>Managing Partner</p>
      <p>contact # 202-555-0147</p>
      <p>martin@twbm.example</p>
      <p class="site">www.twbm.example</p>
    </div>
  </section>

  <!-- Option 3 -->
  <section class="card col-a" style="top:627px;">
    <div class="brand-disc" style="top:17px;">
      <span class="brand-name">twbm</span>
    </div>
    <p class="card-tagline card-tagline--spaced" style="top:167px;">TOWARD BRIGHT MORROW</p>
  </section>
  <section class="card card--teal col-b" style="top:627px; left:596px;">
    <div class="contact" style="top:38px;">
      <p class="person">Martin K Pardo</p>
      <p>Managing Partner</p>
      <p>contact # 202-555-0147</p>
      <p>martin@twbm.example</p>
      <p class="site">www.twbm.example</p>
    </div>
  </section>

  <!-- Option 4 -->
  <section class="card card--teal col-a" style="top:861px;">
    <div class="brand-disc" style="top:34px;">
      <span class="brand-name">twbm</span>
      <span class="brand-tag">toward bright morrow</span>
    </div>
  </section>
  <section class="card col-b" style="top:861px;">
    <div class="contact" style="top:22px;">
      <p class="person">Martin K Pardo</p>
      <p>Managing Partner</p>
      <p>contact # 202-555-0147</p>
      <p>martin@twbm.example</p>
      <p class="site">www.twbm.example</p>
    </div>
    <div class="ribbon-art" role="img" aria-label="Script brand wordmark flowing into a wavy orange ribbon along the bottom edge"></div>
  </section>
</body>
</html>
```